Luminously Grounded Vitality

We want to design a business card that is modern and appealing for an innovative psychedelic telemedicine company that provides at-home ketamine-assisted therapy along with wellness, longevity, and anti-aging medicines. We want to use our deep purple and white plus other colors you can find on our website. We don't have any strict brand guidelines yet so feel free to get creative. We want a very professional, but technology first modern design that will instill trust, peace, calm, but also be attractive to investors in the healthcare and SaaS space.

```html
<!DOCTYPE html>
<html lang="en">
<head>
<meta charset="utf-8">
<title>Luminously Grounded Vitality — Business Card</title>
<link href="https://fonts.googleapis.com/css2?family=Montserrat:wght@400;500;700&display=swap" rel="stylesheet">
<style>
  :root {
    --backdrop: #e4e4e6;
    --card-white: #ffffff;
    --deep-purple: #7a5fb0;
    --purple-dark: #6b4fa3;
    --orchid: #a24f9e;
    --ink: #3d3d45;
    --ink-soft: #5a5a62;
    --pattern-light: #8c72c0;
    --pattern-deep: #5f4298;
  }
  * { margin: 0; padding: 0; box-sizing: border-box; }
  html, body {
    width: 1200px; height: 801px; overflow: hidden;
    background: var(--backdrop);
    font-family: "Montserrat", sans-serif;
  }
  .stage {
    width: 1200px; height: 801px;
    display: flex; align-items: center; justify-content: center; gap: 40px;
  }
  .card {
    width: 540px; height: 309px; position: relative; overflow: hidden;
    box-shadow: 0 10px 28px rgba(0,0,0,0.18);
  }
  /* Front side */
  .card-front { background: var(--card-white); border-bottom: 3px solid var(--deep-purple); }
  .brand-block {
    position: absolute; right: 34px; top: 34px; text-align: right;
    display: flex; align-items: center; gap: 12px;
  }
  .brand-dot { width: 26px; height: 26px; border-radius: 50%; background: var(--deep-purple); }
  .brand-name {
    font-weight: 500; font-size: 19px; color: var(--orchid); letter-spacing: 0.2px;
  }
  .divider {
    position: absolute; left: 34px; right: 34px; top: 128px;
    height: 1.5px; background: var(--deep-purple);
  }
  .person { position: absolute; left: 34px; top: 172px; }
  .person-name {
    font-weight: 700; font-size: 19px; color: var(--deep-purple); letter-spacing: 0.3px;
    text-transform: uppercase;
  }
  .person-role { font-size: 13px; color: var(--ink-soft); margin-top: 2px; }
  .person-rule { width: 250px; height: 1px; background: var(--deep-purple); margin: 10px 0 8px; }
  .contact-list { list-style: none; }
  .contact-list li {
    display: flex; align-items: center; gap: 8px;
    font-size: 12.5px; color: var(--ink); line-height: 20px;
  }
  .contact-list svg { width: 11px; height: 11px; fill: var(--orchid); flex: none; }
  .address {
    position: absolute; right: 34px; top: 146px; text-align: right;
    font-size: 13px; color: var(--ink); line-height: 19px;
  }
  /* Back side */
  .card-back { background: var(--deep-purple); }
  .back-pattern {
    position: absolute; inset: 0;
    background: linear-gradient(120deg, var(--pattern-deep) 0%, var(--deep-purple) 50%, var(--pattern-light) 100%);
  }
  .back-brand {
    position: absolute; left: 150px; top: 140px;
    display: flex; align-items: center; gap: 12px;
  }
  .back-brand .brand-dot { background: var(--card-white); width: 24px; height: 24px; }
  .back-brand .brand-name { color: var(--card-white); font-size: 20px; font-weight: 500; }
</style>
</head>
<body>
<main class="stage">
  <section class="card card-front">
    <div class="brand-block">
      <span class="brand-dot"></span>
      <span class="brand-name">Luminously Grounded Vitality</span>
    </div>
    <div class="divider"></div>
    <div class="address">1180 Cypress Tide Way<br>Seabrook CA 90000</div>
    <div class="person">
      <p class="person-name">Mara Quillen</p>
      <p class="person-role">President</p>
      <div class="person-rule"></div>
      <ul class="contact-list">
        <li><svg viewBox="0 0 24 24"><path d="M6.6 10.8a15 15 0 0 0 6.6 6.6l2.2-2.2a1 1 0 0 1 1-.25 11.4 11.4 0 0 0 3.6.57 1 1 0 0 1 1 1V20a1 1 0 0 1-1 1A17 17 0 0 1 3 4a1 1 0 0 1 1-1h3.5a1 1 0 0 1 1 1c0 1.25.2 2.45.57 3.57a1 1 0 0 1-.25 1z"/></svg>555-014-2287</li>
        <li><svg viewBox="0 0 24 24"><path d="M2 5h20v14H2z M2 5l10 8 10-8" /></svg>hello@luminouslygrounded.com</li>
        <li><svg viewBox="0 0 24 24"><circle cx="12" cy="12" r="10"/></svg>www.luminouslygrounded.com</li>
      </ul>
    </div>
  </section>

  <section class="card card-back">
    <div class="back-pattern" role="img" aria-label="Repeating embossed brand pattern in shades of purple"></div>
    <div class="back-brand">
      <span class="brand-dot"></span>
      <span class="brand-name">Luminously Grounded Vitality</span>
    </div>
  </section>
</main>
</body>
</html>
```